We are looking to design GUI's for an App that works on a Tablet fixed to a wall in a hotel room to control the Internet radio and Marvu speakers. The app is built, and you can see each GUI in the QTRMarvu App.pdf. We need to keep the structure the same, as we don't want to change too much in the code. I have added an image just for you to get a picture of the device. our logo is also included.

```html
<!DOCTYPE html>
<html lang="en">
<head>
<meta charset="utf-8">
<title>QTRMarvu Tablet Screens</title>
<link href="https://fonts.googleapis.com/css2?family=Roboto:wght@400;500;700&display=swap" rel="stylesheet">
<style>
:root{
  --stage-a:#d8bde4;--stage-b:#d6d3dc;--stage-c:#dcbfe6;
  --bar:#151634;--body:#1e1f45;--panel:#1a1b3e;--tile:#24265a;--card:#22234f;
  --text:#ffffff;--muted:#8a8cb0;--dim:#5c5e86;--accent:#a23fd8;--accent-2:#7b3fd0;--source:#2c2e66;
}
*{box-sizing:border-box;margin:0;padding:0}
html,body{width:688px;height:1200px;overflow:hidden}
body{position:relative;font-family:'Roboto',sans-serif;color:var(--text);
  background:linear-gradient(160deg,var(--stage-a) 0%,var(--stage-b) 45%,var(--stage-b) 60%,var(--stage-c) 100%)}
.screen{position:absolute;width:406px;height:238px;background:var(--body);border-radius:2px;overflow:hidden;box-shadow:0 2px 6px rgba(20,20,50,.25)}
.screen.partial{width:111px;height:137px}
.topbar{position:absolute;left:0;top:0;right:0;height:23px;background:var(--bar);display:flex;align-items:center;justify-content:center;font-size:7.5px;letter-spacing:.2px}
.status{position:absolute;right:14px;top:7px;display:flex;align-items:center;gap:5px;font-size:5.5px}
.navbar{position:absolute;left:0;right:0;bottom:0;height:22px;background:var(--bar);display:flex;justify-content:space-around;align-items:center;padding:0 4px}
.navbar svg{width:9px;height:9px}
.selector{position:absolute;left:74px;top:35px;width:258px;height:145px;background:var(--panel);border-radius:3px}
.selector h1{font-size:8px;font-weight:500;text-align:center;margin-top:9px;white-space:nowrap}
.selector p{font-size:4.5px;color:var(--dim);text-align:center;margin-top:3px;white-space:nowrap}
.room{position:absolute;width:59px;height:22px;background:var(--tile);border-radius:2px;font-size:5px;font-weight:700;display:flex;align-items:center;justify-content:center}
.brandrow{position:absolute;left:9px;right:15px;top:194px;display:flex;justify-content:space-between;align-items:center}
.brand{font-size:8px;font-weight:500;color:#b7b8cc;display:flex;align-items:center;gap:4px}
.brand i{width:7px;height:7px;background:#b7b8cc;display:block}
.wordmark{font-size:7px;font-weight:500;letter-spacing:1.5px;color:#9a9cb8}
.player{position:absolute;width:179px;height:112px;background:var(--card);overflow:hidden}
.player .art{position:absolute;left:0;top:0;right:0;height:74px;background:radial-gradient(circle at 75% 35%,#6a33b6 0,#3b2a84 28%,#1d1c45 60%),var(--bar)}
.player .art.blank{background:var(--card)}
.meta{position:absolute;left:10px;top:20px;font-size:6.5px;line-height:11.5px;white-space:nowrap}
.meta span{color:var(--muted);display:inline-block;width:26px;font-size:6px}
.controls{position:absolute;left:0;right:0;bottom:0;height:38px;background:var(--panel);display:flex;justify-content:center;align-items:center;gap:26px}
.play{width:24px;height:24px;border-radius:50%;background:linear-gradient(135deg,var(--accent),var(--accent-2));display:flex;align-items:center;justify-content:center}
.cover{position:absolute;left:17px;top:38px;width:162px;height:161px;border-radius:2px;background:linear-gradient(180deg,#7a56b8 0%,#5a3a8e 35%,#7b2c4e 70%,#3a2a6b 100%)}
.cover.empty{background:var(--panel);display:flex;align-items:center;justify-content:center}
.volume{position:absolute;left:203px;top:178px;width:179px;height:14px;display:flex;align-items:center}
.slider{position:relative;margin-left:6px;width:115px;height:2px;background:#3a3c6a;border-radius:1px}
.slider b{position:absolute;left:0;top:0;height:2px;width:82%;background:linear-gradient(90deg,var(--accent-2),var(--accent))}
.slider b::after{content:"";position:absolute;right:-2.5px;top:-1.5px;width:5px;height:5px;border-radius:50%;background:#c58cf0}
.volume .src{position:absolute;width:13px;height:13px}
.station{position:absolute;width:204px;height:58px;background:var(--card);overflow:hidden}
.station .thumb{position:absolute;left:0;top:0;width:67px;height:58px}
.station h2{position:absolute;left:76px;top:14px;font-size:7px;font-weight:400;white-space:nowrap}
.station p{position:absolute;left:76px;top:26px;font-size:5px;color:var(--dim);font-weight:500;white-space:nowrap}
.station .tag{position:absolute;right:4px;top:4px;font-size:4.5px;letter-spacing:1px;color:var(--muted)}
.source-tile{position:absolute;left:98px;top:0;width:81px;height:74px;background:var(--source);display:flex;align-items:center;justify-content:center;font-size:7px;font-weight:500;color:var(--text);white-space:nowrap}
</style>
</head>
<body>
<svg width="0" height="0" style="position:absolute">
  <defs>
    <symbol id="i-down" viewBox="0 0 10 10"><path d="M2 2l3 3 3-3M2 5l3 3 3-3" fill="none" stroke="#fff" stroke-width="1.2"/></symbol>
    <symbol id="i-mute" viewBox="0 0 10 10"><path d="M1 4h2l3-2.5v7L3 6H1z" fill="#fff"/><path d="M7 4.2l2 2M9 4.2l-2 2" stroke="#fff" stroke-width=".8"/></symbol>
    <symbol id="i-back" viewBox="0 0 10 10"><path d="M7 1.5L2.5 5 7 8.5z" fill="none" stroke="#fff" stroke-width="1"/></symbol>
    <symbol id="i-home" viewBox="0 0 10 10"><circle cx="5" cy="5" r="3.8" fill="none" stroke="#fff" stroke-width="1"/></symbol>
    <symbol id="i-recent" viewBox="0 0 10 10"><rect x="1.8" y="1.8" width="6.4" height="6.4" fill="none" stroke="#fff" stroke-width="1"/></symbol>
    <symbol id="i-vol" viewBox="0 0 10 10"><path d="M1 4h2l3-2.5v7L3 6H1z" fill="#fff"/><path d="M7.5 3.5v3M9 2.5v5" stroke="#fff" stroke-width=".8" stroke-dasharray="1 .6"/></symbol>
    <symbol id="i-power" viewBox="0 0 10 10"><path d="M3 2.6a3.6 3.6 0 1 0 4 0" fill="none" stroke="#fff" stroke-width="1"/><path d="M5 1v4" stroke="#fff" stroke-width="1"/></symbol>
    <symbol id="i-wifi" viewBox="0 0 12 9"><path d="M1 3a7 7 0 0 1 10 0M2.8 4.8a4.5 4.5 0 0 1 6.4 0M4.5 6.5a2 2 0 0 1 3 0" fill="none" stroke="#fff" stroke-width="1"/></symbol>
    <symbol id="i-prev" viewBox="0 0 10 10"><path d="M2 2v6" stroke="currentColor" stroke-width="1.2"/><path d="M8 2L3.5 5 8 8z" fill="currentColor"/></symbol>
    <symbol id="i-next" viewBox="0 0 10 10"><path d="M8 2v6" stroke="currentColor" stroke-width="1.2"/><path d="M2 2l4.5 3L2 8z" fill="currentColor"/></symbol>
    <symbol id="i-pause" viewBox="0 0 16 18"><rect x="1" y="0" width="4.5" height="18" fill="#fff"/><rect x="10.5" y="0" width="4.5" height="18" fill="#fff"/></symbol>
    <symbol id="i-playtri" viewBox="0 0 10 10"><path d="M3 1.5l5.5 3.5L3 8.5z" fill="#fff"/></symbol>
    <symbol id="i-radio" viewBox="0 0 14 14"><path d="M2 5h10v7H2z" fill="#fff"/><path d="M3 5l8-3" stroke="#fff" stroke-width="1"/><circle cx="4.5" cy="9.5" r="1.2" fill="#1e1f45"/><path d="M7 7.5h4" stroke="#1e1f45" stroke-width="1"/></symbol>
    <symbol id="i-speaker" viewBox="0 0 14 14"><rect x="3" y="1" width="8" height="12" rx="1" fill="#fff"/><circle cx="7" cy="8.8" r="2.2" fill="#1e1f45"/><circle cx="7" cy="3.6" r=".9" fill="#1e1f45"/></symbol>
  </defs>
</svg>

<section class="screen" style="left:44px;top:43px">
  <header class="topbar">QTR<div class="status"><svg width="9" height="7"><use href="#i-wifi"/></svg>09:43</div></header>
  <div class="selector">
    <h1>QTRMarvu Speaker Selector</h1>
    <p>Please select a speaker to start</p>
  </div>
  <div class="room" style="left:103px;top:82px">PATIO</div>
  <div class="room" style="left:173px;top:82px">MARVU MOVE</div>
  <div class="room" style="left:243px;top:82px">KITCHEN</div>
  <div class="room" style="left:103px;top:114px">ROOM #3</div>
  <div class="brandrow"><div class="brand"><i></i>Roomwave</div><div class="wordmark">MARVU</div></div>
  <nav class="navbar"><svg><use href="#i-down"/></svg><svg><use href="#i-mute"/></svg><svg><use href="#i-back"/></svg><svg><use href="#i-home"/></svg><svg><use href="#i-recent"/></svg><svg><use href="#i-vol"/></svg><svg><use href="#i-power"/></svg></nav>
</section>

<section class="screen partial" style="left:577px;top:83px">
  <div class="selector" style="left:0;top:0;width:111px;height:137px">
    <h1 style="text-align:left;padding-left:78px">QTRMarvu</h1>
    <p style="text-align:left;padding-left:93px">Please</p>
  </div>
  <div class="room" style="left:30px;top:46px">PATIO</div>
  <div class="room" style="left:100px;top:46px;width:11px"></div>
  <div class="room" style="left:30px;top:78px">ROOM #3</div>
</section>

<div class="player" style="left:15px;top:371px">
  <div class="art" role="img" aria-label="Purple synthwave sunset over mountains"></div>
  <div class="meta"><div><span>Title:</span>Orbit</div><div><span>Artist:</span>Daren Kolm</div><div><span>Album:</span>Horizons</div></div>
  <div class="controls"><svg width="9" height="9" color="#5c5e86"><use href="#i-prev"/></svg><svg width="16" height="18"><use href="#i-pause"/></svg><svg width="9" height="9" color="#fff"><use href="#i-next"/></svg></div>
</div>

<section class="screen" style="left:230px;top:326px">
  <header class="topbar">KITCHEN<div class="status"><svg width="9" height="7"><use href="#i-wifi"/></svg>09:43</div></header>
  <div class="cover" role="img" aria-label="Album cover: purple mountain road with a glass sphere"></div>
  <div class="player" style="left:203px;top:46px">
    <div class="art" role="img" aria-label="Purple synthwave sunset over mountains"></div>
    <div class="meta"><div><span>Title:</span>Orbit</div><div><span>Artist:</span>Daren Kolm</div><div><span>Album:</span>Horizons</div></div>
    <div class="controls"><svg width="9" height="9" color="#5c5e86"><use href="#i-prev"/></svg><svg width="16" height="18"><use href="#i-pause"/></svg><svg width="9" height="9" color="#fff"><use href="#i-next"/></svg></div>
  </div>
  <div class="volume"><svg width="8" height="8"><use href="#i-vol"/></svg><div class="slider"><b></b></div>
    <svg class="src" style="left:143px"><use href="#i-radio"/></svg><svg class="src" style="left:168px"><use href="#i-speaker"/></svg></div>
  <nav class="navbar"><svg><use href="#i-down"/></svg><svg><use href="#i-mute"/></svg><svg><use href="#i-back"/></svg><svg><use href="#i-home"/></svg><svg><use href="#i-recent"/></svg><svg><use href="#i-vol"/></svg><svg><use href="#i-power"/></svg></nav>
</section>

<section class="screen" style="left:48px;top:608px">
  <header class="topbar">QTR<div class="status"><svg width="9" height="7"><use href="#i-wifi"/></svg>09:43</div></header>
  <div class="selector" style="top:31px;height:220px">
    <h1>QTRMarvu Radio Selector</h1>
    <p>Please select a speaker to start</p>
  </div>
  <div class="station" style="left:100px;top:67px"><div class="thumb" role="img" aria-label="Colourful collage station artwork" style="background:linear-gradient(135deg,#c9a43a,#3a6a8a 50%,#d8662a)"></div><span class="tag">MARVU</span><h2>Hit List</h2><p>Marvu Radio Station</p></div>
  <div class="station" style="left:100px;top:134px"><div class="thumb" role="img" aria-label="Pink flower station artwork" style="background:radial-gradient(circle,#f3d6dc 0 35%,#ad5a5e 60%)"></div><span class="tag">MARVU</span><h2>Cover List</h2><p>Marvu Radio Station</p></div>
  <div class="station" style="left:100px;top:201px"><div class="thumb" role="img" aria-label="Orange ring pattern station artwork" style="background:linear-gradient(90deg,#e8652a,#f2b07a)"></div><span class="tag">MARVU</span><h2 style="top:13px">Classic List</h2></div>
  <nav class="navbar"><svg><use href="#i-down"/></svg><svg><use href="#i-mute"/></svg><svg><use href="#i-back"/></svg><svg><use href="#i-home"/></svg><svg><use href="#i-recent"/></svg><svg><use href="#i-vol"/></svg><svg><use href="#i-power"/></svg></nav>
</section>

<div class="station" style="left:504px;top:674px;width:184px"><div class="thumb" role="img" aria-label="Colourful collage station artwork" style="background:linear-gradient(135deg,#c9a43a,#3a6a8a 50%,#d8662a)"></div><h2>Hit List</h2><p>Marvu Radio Station</p></div>

<div class="player" style="left:15px;top:961px">
  <div class="art blank"></div>
  <div class="meta"><div><span>Title:</span>-</div><div><span>Artist:</span>-</div><div><span>Album:</span>-</div></div>
  <div class="controls"><svg width="9" height="9" color="#5c5e86"><use href="#i-prev"/></svg><div class="play"><svg width="10" height="10"><use href="#i-playtri"/></svg></div><svg width="9" height="9" color="#5c5e86"><use href="#i-next"/></svg></div>
</div>

<section class="screen" style="left:240px;top:890px">
  <header class="topbar">KITCHEN<div class="status"><svg width="9" height="7"><use href="#i-wifi"/></svg>09:43</div></header>
  <div class="cover empty"><svg width="64" height="64" viewBox="0 0 64 64"><circle cx="27" cy="44" r="12" fill="#262752"/><path d="M35 44V16h14v9H39" fill="none" stroke="#262752" stroke-width="6"/><path d="M6 6l52 52" stroke="#262752" stroke-width="5" stroke-linecap="round"/></svg></div>
  <div class="player" style="left:203px;top:46px">
    <div class="art blank"></div>
    <div class="meta"><div><span>Title:</span>-</div><div><span>Artist:</span>-</div><div><span>Album:</span>-</div></div>
    <div class="source-tile">Marvu Radio</div>
    <div class="controls"><svg width="9" height="9" color="#5c5e86"><use href="#i-prev"/></svg><div class="play"><svg width="10" height="10"><use href="#i-playtri"/></svg></div><svg width="9" height="9" color="#5c5e86"><use href="#i-next"/></svg></div>
  </div>
  <div class="volume"><svg width="8" height="8"><use href="#i-vol"/></svg><div class="slider"><b></b></div>
    <svg class="src" style="left:143px"><use href="#i-radio"/></svg><svg class="src" style="left:168px"><use href="#i-speaker"/></svg></div>
  <nav class="navbar"><svg><use href="#i-down"/></svg><svg><use href="#i-mute"/></svg><svg><use href="#i-back"/></svg><svg><use href="#i-home"/></svg><svg><use href="#i-recent"/></svg><svg><use href="#i-vol"/></svg><svg><use href="#i-power"/></svg></nav>
</section>
</body>
</html>
```